New Business Card Design Project

Use the flyer uploaded and website www.brightoakbuilders.example for inspiration.
List Our Services on Backside of business cards
Marcus Dell
Harborline Renovations Inc.
Licensed General Contractors
555-014-7390

Contact Information for Business Card

Use the flyer uploaded and website www.brightoakbuilders.example for inspiration. List Our Services on Backside of business cards Marcus Dell Harborline Renovations Inc. Licensed General Contractors 555-014-7390

```html
<!DOCTYPE html>
<html lang="en">
<head>
<meta charset="utf-8">
<title>Harborline Renovations – Business Card</title>
<link rel="stylesheet" href="https://fonts.googleapis.com/css2?family=Tinos:wght@400;700&display=swap">
<style>
  :root {
    --backdrop: #7d7f82;
    --card: #141414;
    --ink: #f2f2f2;
    --rule: #2f6f95;
  }
  * { margin: 0; padding: 0; box-sizing: border-box; }
  html, body { width: 1200px; height: 900px; overflow: hidden; }
  body {
    background: var(--backdrop);
    font-family: "Tinos", "Times New Roman", serif;
    color: var(--ink);
    display: flex;
    align-items: center;
    justify-content: center;
    gap: 70px;
  }
  .card {
    width: 360px;
    height: 630px;
    background: var(--card);
    border-radius: 3px;
    box-shadow: 0 10px 24px rgba(0,0,0,.35);
    display: flex;
    flex-direction: column;
    align-items: center;
    text-align: center;
    padding: 120px 28px 0;
  }
  .brand {
    display: flex;
    align-items: center;
    gap: 10px;
    font-size: 21px;
    letter-spacing: 2px;
    text-transform: uppercase;
    font-weight: 400;
  }
  .brand-mark {
    width: 14px;
    height: 14px;
    border: 1.5px solid var(--ink);
  }
  .rule {
    width: 270px;
    height: 1px;
    background: var(--rule);
    margin: 14px 0;
  }
  .person-name {
    font-size: 36px;
    font-weight: 700;
    letter-spacing: 1px;
    line-height: 1.05;
  }
  .company, .licence {
    font-size: 23px;
    line-height: 1.15;
  }
  .call-to-action {
    font-size: 44px;
    line-height: 1.0;
    margin-top: 2px;
  }
  .phone {
    display: flex;
    align-items: center;
    gap: 14px;
    font-size: 36px;
    margin-top: 6px;
  }
  .phone svg { width: 30px; height: 30px; }
  .website {
    font-size: 19px;
    margin-top: 14px;
  }
  .services-title {
    font-size: 32px;
    letter-spacing: 1px;
    margin-bottom: 6px;
  }
  .service-list {
    list-style: none;
    font-size: 19.5px;
    line-height: 1.27;
  }
  .service-list .large { font-size: 25px; line-height: 1.05; }
  .guarantee {
    font-size: 27px;
    font-weight: 700;
    line-height: 1.1;
  }
</style>
</head>
<body>

  <section class="card card-front" aria-label="Front of business card">
    <div class="brand"><span class="brand-mark"></span>Harborline</div>
    <div class="rule"></div>
    <h1 class="person-name">MARCUS DELL</h1>
    <p class="company">Harborline Renovations Inc.</p>
    <p class="licence">Licensed General Contractors</p>
    <div class="rule"></div>
    <p class="call-to-action">Call/Text Or<br>Book Online</p>
    <p class="phone">
      <svg viewBox="0 0 24 24" aria-hidden="true">
        <path d="M6.6 3.5l2.6 3.6-1.7 2.1c.9 2.2 2.9 4.3 5.2 5.3l2.1-1.7 3.6 2.6-1.2 3.3c-6.9.2-13-5.9-12.8-12.8z" fill="none" stroke="#f2f2f2" stroke-width="1.8" stroke-linejoin="round"/>
        <path d="M14 4.5a5.5 5.5 0 0 1 5.5 5.5M14 8a2 2 0 0 1 2 2" fill="none" stroke="#f2f2f2" stroke-width="1.6" stroke-linecap="round"/>
      </svg>
      555-014-7390
    </p>
    <p class="website">www.brightoakbuilders.example</p>
  </section>

  <section class="card card-back" aria-label="Back of business card">
    <div class="brand"><span class="brand-mark"></span>Harborline</div>
    <div class="rule"></div>
    <h2 class="services-title">OUR SERVICES</h2>
    <ul class="service-list">
      <li>Remodel - Kitchen &amp; Bath</li>
      <li>Painting - Interior &amp; Exterior</li>
      <li>Flooring - Carpet, Vinyl, Wood</li>
      <li>Window &amp; Door Replacement</li>
      <li>Plumbing - Repairs &amp; Upgrades</li>
      <li>Energy - Efficient Upgrades</li>
      <li>Deck &amp; Patio Construction</li>
      <li class="large">Water &amp; Mold Damage</li>
      <li class="large">Garage Renovation</li>
    </ul>
    <div class="rule"></div>
    <p class="guarantee">Our Services Are<br>100% Guaranteed</p>
  </section>

</body>
</html>
```